Mortgage Broker Site

Need a custom design for a mortgage broker site - please refer to the attached Word .doc that gives more detail.

Number of Pages Required

5+ page

Colors

Designer to choose colors to be used in the design.

```html
<!DOCTYPE html>
<html lang="en">
<head>
<meta charset="utf-8">
<title>Kestora Mortgage</title>
<link href="https://fonts.googleapis.com/css2?family=Poppins:wght@300;400;500;600&display=swap" rel="stylesheet">
<style>
:root{
  --red:#ad0f1d;
  --red-bright:#c8101f;
  --ink:#1f1f1f;
  --text:#2b2b2b;
  --footer:#121212;
  --footer-text:#d8d8d8;
  --white:#ffffff;
  --tint:#e9e9ef;
}
*{margin:0;padding:0;box-sizing:border-box}
html,body{width:672px;height:1200px;overflow:hidden}
body{font-family:'Poppins',sans-serif;color:var(--text);background:var(--white);position:relative}
.abs{position:absolute}
.center{left:0;right:0;text-align:center}

/* hero */
.hero{position:absolute;left:0;top:0;width:672px;height:311px}
.hero-photo{position:absolute;inset:0;background:linear-gradient(100deg,#2a2420 0%,#3a322b 45%,#5a4d40 75%,#3a3129 100%)}
.hero-shade{position:absolute;inset:0;background:linear-gradient(90deg,rgba(0,0,0,.45),rgba(0,0,0,.1))}
.nav-line{position:absolute;left:0;right:0;top:43px;height:1px;background:rgba(255,255,255,.15)}
.brand{position:absolute;left:52px;top:11px;font-size:19px;font-weight:500;color:var(--white);line-height:22px}
.nav{position:absolute;top:17px;font-size:8px;font-weight:500;color:var(--white)}
.schedule{position:absolute;left:462px;top:17px;font-size:8px;font-weight:500;color:var(--white);display:flex;align-items:center;gap:4px}
.apply{position:absolute;left:551px;top:13px;width:70px;height:19px;background:var(--red-bright);color:var(--white);font-size:8px;font-weight:500;display:flex;align-items:center;justify-content:center;border-radius:2px}
.hero-title{position:absolute;left:52px;top:110px;font-size:20px;font-weight:600;line-height:24px;color:var(--white)}
.hero-copy{position:absolute;left:51px;top:172px;width:340px;font-size:7.4px;font-weight:300;line-height:12.8px;color:var(--white)}
.btn{position:absolute;top:228px;width:96px;height:27px;background:var(--red);color:var(--white);font-size:7.4px;display:flex;align-items:center;justify-content:center;border-radius:2px}

/* tools */
.section-title{font-size:18px;font-weight:400;color:var(--ink)}
.rule{position:absolute;height:2px;left:50%;transform:translateX(-50%)}
.lead{font-size:8px;line-height:13px;color:var(--ink)}
.tool-icon{position:absolute;top:459px;width:40px;height:40px;border-radius:50%;background:var(--tint);display:flex;align-items:center;justify-content:center}
.tool-title{position:absolute;top:506px;width:250px;text-align:center;font-size:11px;color:var(--ink)}
.tool-copy{position:absolute;top:530px;width:250px;text-align:center;font-size:8px;line-height:10.5px;color:var(--ink)}
.divider{position:absolute;width:1px;background:#e2e2e2}

/* limits */
.limits{position:absolute;left:0;top:600px;width:672px;height:202px}
.limits-photo{position:absolute;inset:0;background:linear-gradient(110deg,#3a3936 0%,#4a4843 40%,#33322f 70%,#2a2927 100%)}
.limits-shade{position:absolute;inset:0;background:rgba(0,0,0,.35)}
.search{position:absolute;left:205px;top:133px;width:262px;height:17px;background:var(--white);border-radius:9px;display:flex;align-items:center;padding-left:7px;gap:5px;font-size:6px;color:#8a8a8a}

/* connect */
.skyline{position:absolute;left:0;top:836px;width:672px;height:111px;background:linear-gradient(180deg,rgba(238,238,238,0) 0%,#f0f0f0 55%,#efefef 100%)}
.phone-big{position:absolute;top:877px;font-size:18px;font-weight:600;color:var(--red);display:flex;align-items:center;justify-content:center;gap:6px}

/* footer */
.footer{position:absolute;left:0;top:947px;width:672px;height:253px;background:var(--footer)}
.f-head{position:absolute;top:44px;font-size:14px;font-weight:500;color:var(--white)}
.f-list{position:absolute;top:76px;list-style:none}
.f-list li{font-size:8px;font-weight:300;color:var(--footer-text);height:18px;display:flex;align-items:center;gap:7px}
.f-list li::before{content:"";width:3px;height:3px;border-right:1px solid var(--footer-text);border-top:1px solid var(--footer-text);transform:rotate(45deg)}
.f-div{position:absolute;top:47px;width:1px;height:96px;background:#3a3a3a}
.social{position:absolute;top:178px;left:296px;display:flex;gap:4.5px}
.social span{width:17px;height:17px;border-radius:50%;background:var(--white)}
.nmls{position:absolute;top:202px;font-size:8px;font-weight:300;color:var(--footer-text)}
.f-line{position:absolute;left:0;right:0;top:217px;height:1px;background:#333}
.copyright{position:absolute;top:229px;font-size:8px;font-weight:300;color:var(--footer-text);white-space:nowrap}
.to-top{position:absolute;left:632px;top:186px;width:22px;height:22px;border-radius:50%;background:var(--red-bright);box-shadow:0 0 0 2px rgba(200,16,31,.25);display:flex;align-items:center;justify-content:center}
</style>
</head>
<body>

<header class="hero">
  <div class="hero-photo" role="img" aria-label="Photo of a person working on a calculator and paperwork at a desk"></div>
  <div class="hero-shade"></div>
  <div class="nav-line"></div>
  <div class="brand">Kestora</div>
  <nav>
    <span class="nav" style="left:151px">Rates</span>
    <span class="nav" style="left:194px">Purchase</span>
    <span class="nav" style="left:251px">Refinance</span>
    <span class="nav" style="left:312px">Guides</span>
  </nav>
  <div class="schedule">
    <svg width="8" height="8" viewBox="0 0 24 24"><path fill="#fff" d="M6.6 10.8a15 15 0 0 0 6.6 6.6l2.2-2.2c.3-.3.7-.4 1-.2 1.1.4 2.3.6 3.6.6.6 0 1 .4 1 1V20c0 .6-.4 1-1 1A17 17 0 0 1 3 4c0-.6.4-1 1-1h3.5c.6 0 1 .4 1 1 0 1.3.2 2.5.6 3.6.1.3 0 .7-.2 1z"/></svg>
    Schedule a call
  </div>
  <div class="apply">Apply now</div>
  <h1 class="hero-title">When all the doors are closed,<br>you will find our’s open</h1>
  <p class="hero-copy">Top up personal loan is a facility provided by financial institutions to customers that allows you to borrow a certain amount of money over your personal loan. The interest rate for a top up loan is slightly higher than the regular personal loan.</p>
  <div class="btn" style="left:52px">PURCHASE RATES</div>
  <div class="btn" style="left:157px">REFINANCE RATES</div>
</header>

<section class="tools">
  <h2 class="abs center section-title" style="top:355px">Mortgage Tools</h2>
  <div class="rule" style="top:387px;width:17px;background:var(--red)"></div>
  <p class="abs center lead" style="top:402px">Fimply dummy text of the printing and typesetting industry. Lorem Ipsum has been the<br>industry's standardever since unknown printer took a galley.</p>

  <div class="tool-icon" style="left:192px">
    <svg width="22" height="22" viewBox="0 0 24 24" fill="none" stroke="#ad0f1d" stroke-width="1.3"><path d="M4 10l8-6 8 6"/><path d="M6 9v6h12V9"/><circle cx="12" cy="12" r="2.5"/><path d="M3 19c3-2 6-2 9 0h6l3-2"/></svg>
  </div>
  <div class="tool-title" style="left:86px">Mortgage Calculator</div>
  <div class="tool-copy" style="left:86px">See how much you can afford by home price,<br>monthly payment, on income</div>

  <div class="divider" style="left:336px;top:461px;height:95px"></div>

  <div class="tool-icon" style="left:440px">
    <svg width="22" height="22" viewBox="0 0 24 24" fill="none" stroke="#ad0f1d" stroke-width="1.3"><rect x="5" y="4" width="11" height="15" rx="1"/><path d="M8 13h5M8 16h4"/><path d="M10.5 6v5M9 7.5h3"/><circle cx="17" cy="17" r="3.5"/><path d="M15.5 17l1 1 2-2"/></svg>
  </div>
  <div class="tool-title" style="left:335px">Mortgage Calculator</div>
  <div class="tool-copy" style="left:335px">See how much you can afford by home price,<br>monthly payment, on income</div>
</section>

<section class="limits">
  <div class="limits-photo" role="img" aria-label="Photo of hands signing a loan document beside a calculator"></div>
  <div class="limits-shade"></div>
  <h2 class="abs center" style="top:44px;font-size:15px;font-weight:400;color:var(--white)">2019 Mortgage Loan Limits For Conventional, FHA, &amp; VA Loans</h2>
  <div class="rule" style="top:72px;width:28px;background:var(--white)"></div>
  <p class="abs center" style="top:87px;font-size:8px;line-height:13px;color:var(--white)">Mortgage loan limits for every U.s country, as published by Homestead Fund &amp; Keystone Home Co, the Federal Housing Administration (FHA), and the<br>Department of Veterans Affairs (VA)</p>
  <div class="search">
    <svg width="8" height="8" viewBox="0 0 24 24" fill="none" stroke="#555" stroke-width="2.5"><circle cx="10" cy="10" r="7"/><path d="M15 15l6 6"/></svg>
    Search for loan...
  </div>
</section>

<section class="connect">
  <div class="skyline" role="img" aria-label="Faint city skyline silhouette"></div>
  <h2 class="abs center" style="top:850px;font-size:16px;font-weight:400;color:var(--ink)">Connect with American's Lending Experts Today!</h2>
  <div class="phone-big center">
    <svg width="17" height="17" viewBox="0 0 24 24"><path fill="#ad0f1d" d="M6.6 10.8a15 15 0 0 0 6.6 6.6l2.2-2.2c.3-.3.7-.4 1-.2 1.1.4 2.3.6 3.6.6.6 0 1 .4 1 1V20c0 .6-.4 1-1 1A17 17 0 0 1 3 4c0-.6.4-1 1-1h3.5c.6 0 1 .4 1 1 0 1.3.2 2.5.6 3.6.1.3 0 .7-.2 1z"/></svg>
    (555)014-2270
  </div>
</section>

<footer class="footer">
  <h3 class="f-head" style="left:51px">Useful Links</h3>
  <ul class="f-list" style="left:52px">
    <li>Get a Mortgage Rate Now</li>
    <li>Loan Types</li>
    <li>Kestora Disclosures</li>
    <li>Conforming, VA &amp; FHA Loan Limits</li>
  </ul>
  <div class="f-div" style="left:224px"></div>
  <h3 class="f-head" style="left:249px">Company</h3>
  <ul class="f-list" style="left:252px">
    <li>About Us</li>
    <li>Careers</li>
    <li>Kestora Resources</li>
    <li>Contact</li>
  </ul>
  <div class="f-div" style="left:448px"></div>
  <h3 class="f-head" style="left:473px">Policies</h3>
  <ul class="f-list" style="left:474px">
    <li>Security Policy</li>
    <li>Privacy Policy</li>
    <li>Terms of Use</li>
    <li>Email Policy</li>
  </ul>
  <div class="social" aria-label="Social links"><span></span><span></span><span></span><span></span></div>
  <p class="nmls center">Kestora NMLS #418206. Click here to view our licensing with the NMLS and DRE</p>
  <div class="f-line"></div>
  <p class="copyright center">2009-2019 Copyright Kestora, Inc. All rights reserved. Lending services provided by Kestora, Inc dba Kestora. Rates, program terms an</p>
  <div class="to-top">
    <svg width="9" height="9" viewBox="0 0 24 24" fill="none" stroke="#fff" stroke-width="2.5"><path d="M5 15l7-7 7 7"/></svg>
  </div>
</footer>

</body>
</html>
```